Buch-/eBook-Cover für Esoterikbuch
Alle meine Änderungswünsche wurden zeitnah umgesetzt. Als es nach der Dateiübergabe technische Probleme gab, weil ich den Buchinhalt falsch formatiert hatte, hat die Designerin viel Geduld bewiesen und das Cover dann klaglos an die neuen Formate angepasst. Ich werde jederzeit gerne wieder mit ihr zusammenarbeiten.
Zielgruppe
Ebook- und Taschenbuchcover für ein Esoterikbuch über Quantenheilung auf Lesora. Details befinden sich im Anhang.
Aufgabenstellung
Keine besonderen Vorgaben.

```html
<!DOCTYPE html>
<html lang="de">
<head>
<meta charset="utf-8">
<title>Quantenheilung und Bewusstsein – Buchcover</title>
<link rel="stylesheet" href="https://fonts.googleapis.com/css2?family=Barlow:wght@400;500;600;800;900&display=swap">
<style>
  :root {
    --ink-deep: #04070b;
    --night: #0a1a26;
    --glow-cyan: #3fc7ee;
    --glow-amber: #e08a4e;
    --magenta: #e4007f;
    --paper-white: #f4f8fb;
  }
  html, body {
    margin: 0;
    padding: 0;
    width: 750px;
    height: 1200px;
    overflow: hidden;
    background: var(--ink-deep);
  }
  .cover {
    position: relative;
    width: 750px;
    height: 1200px;
    overflow: hidden;
    background: var(--ink-deep);
    font-family: "Barlow", "Helvetica Neue", Arial, sans-serif;
  }
  .cover-art {
    position: absolute;
    inset: 0 0 180px 0;
    background:
      radial-gradient(ellipse 180px 160px at 360px 390px, rgba(224,138,78,0.55), transparent 70%),
      radial-gradient(ellipse 120px 120px at 150px 380px, rgba(63,199,238,0.7), transparent 75%),
      radial-gradient(ellipse 300px 330px at 410px 430px, rgba(63,199,238,0.45), transparent 72%),
      radial-gradient(ellipse 520px 520px at 380px 420px, rgba(20,70,100,0.6), transparent 75%),
      linear-gradient(180deg, #06101a 0%, var(--night) 40%, #07121b 75%, var(--ink-deep) 100%);
  }
  .author {
    position: absolute;
    top: 40px;
    left: 0;
    width: 750px;
    text-align: center;
    margin: 0;
    color: var(--paper-white);
    font-weight: 600;
    font-size: 37px;
    letter-spacing: 2.2px;
    line-height: 1;
  }
  .title {
    position: absolute;
    left: 30px;
    top: 688px;
    width: 700px;
    margin: 0;
    color: var(--magenta);
    font-weight: 900;
    text-transform: uppercase;
    line-height: 1;
  }
  .title-line {
    display: block;
    position: absolute;
    left: 0;
    white-space: nowrap;
  }
  .title-quanten { top: -8px; font-size: 148px; letter-spacing: 6px; }
  .title-heilung { top: 129px; font-size: 148px; letter-spacing: 6px; }
  .title-und {
    position: absolute;
    left: 603px;
    top: 187px;
    width: 110px;
    height: 52px;
    line-height: 52px;
    text-align: center;
    font-size: 52px;
    font-weight: 900;
    letter-spacing: 1px;
    transform: rotate(-90deg);
    transform-origin: center center;
    white-space: nowrap;
  }
  .title-bewusstsein { top: 278px; font-size: 95px; letter-spacing: 1.5px; }
  .subtitle {
    position: absolute;
    left: 0;
    top: 1071px;
    width: 750px;
    margin: 0;
    text-align: center;
    color: var(--magenta);
    font-weight: 500;
    font-size: 29px;
    letter-spacing: 1.2px;
    line-height: 40px;
    text-transform: uppercase;
  }
</style>
</head>
<body>
  <main class="cover">
    <div class="cover-art" role="img" aria-label="Leuchtendes Profil eines menschlichen Kopfes mit Gehirn aus blauen und orangen Nervenbahnen vor dunklem, kosmischem Hintergrund"></div>
    <p class="author">LUKAS MONDREITER</p>
    <h1 class="title">
      <span class="title-line title-quanten">Quanten</span>
      <span class="title-line title-heilung">Heilung</span>
      <span class="title-und">und</span>
      <span class="title-line title-bewusstsein">Bewusstsein</span>
    </h1>
    <p class="subtitle">Wie Sie Zugriff auf die Informationsebene<br>der Realität nehmen</p>
  </main>
</body>
</html>
```